Digital Marketing Online Shop Needs a Home Page Web Design

Here is some background on the new home page and the message we want to relay to people visiting our site.
The new site design will be very similar to the following sites
http://plivora.com/
https://quillmarsh.com/
http://barelytidy.io/
http://craftturnip.com/
http://clipmelon.com/
We are a small marketing agency of 3 and we have built up and impressive contact list of partners over the last 16 years to help our customers take their digital marketing to the next level.
The four core areas of products we will be promoting and selling through our online shop are the following :
Web design
Content marketing
Graphic design
Coaching
We operate our agency in a new way, not the old school way so our customers can receive on-demand marketing.
We plan to have an online shop so visitors can purchase some of our services, very similar to how Quill Marshing and Craft Turnip offer their services.
In the end, we want the same call to action layout as Plivora, Quill Marsh and Craft Turnip, however, since we are an agency we would like to blend in Barely Tidy's layout.
We want the customer to either contact us about our services or purchase one of the services from our shop.
We are trying to make the whole digital marketing experience more transactional like retail and not so traditional servicey. :-)
It is from our years of experience and finding the right partners that allows us to offer this type of solution to businesses in the Maritime Provinces (New Brunswick, Nova Scotia, Prince Edward Island, Canada).
Also, because we are offering more of an on-demand/self serve option and we have lower overhead, we hope to pass along great pricing to our customers for their marketing needs. We really want this offer to expand outside of our local market in Saint John, New Brunswick.
I would also like to have a call to action written for a hero image at the top of the page, like the Plivora site.
After that I would like the content to flow through similar to Quill Marsh & Plivora. But mix in some of the agency like content you see with Clipmelon, Barely Tidy.
I have also included the first draft of the content for our home page.
Menu Items will be About, How We Work, Learn, Shop, Contact
Please let me know if you need anything else.
Small businesses, 1-10 person companies with up to 5 million in revenue. Mostly service companies, but some retail.
Marketing
1 page

```html
<!DOCTYPE html>
<html lang="en">
<head>
<meta charset="utf-8">
<title>Tidewell Studio — Home</title>
<link href="https://fonts.googleapis.com/css2?family=Josefin+Sans:wght@600;700&family=Open+Sans:ital,wght@0,400;0,600;0,700;1,700&family=Lato:wght@400;700&display=swap" rel="stylesheet">
<style>
:root{
  --blue:#1f74c9;
  --blue-text:#2f86d6;
  --quote:#1b6ea6;
  --dark:#323438;
  --footer:#1e2026;
  --footer-bar:#1a1c21;
  --white:#ffffff;
  --ink:#2b2b2b;
  --muted:#9a9a9a;
}
*{box-sizing:border-box;margin:0;padding:0}
html,body{width:1200px;height:3636px;overflow:hidden}
body{font-family:'Lato',sans-serif;color:var(--ink);background:var(--white);position:relative}
section,footer,header{position:absolute;left:0;width:1200px}
.abs{position:absolute}
.center{left:0;width:1200px;text-align:center}
.btn{position:absolute;height:40px;border-radius:20px;border:2px solid var(--white);color:var(--white);font:700 12px 'Open Sans',sans-serif;letter-spacing:1.5px;display:flex;align-items:center;justify-content:center;text-transform:uppercase}
.btn.solid{background:var(--white);color:var(--blue)}
.btn.solid.dark{color:#333}

/* hero */
.hero{top:0;height:606px;overflow:hidden}
.hero-photo{position:absolute;inset:0;background:linear-gradient(135deg,#6f8fb3 0%,#8aa6c6 35%,#5d7fa8 60%,#7894b6 100%)}
.brand{left:110px;top:32px;color:var(--white)}
.brand-name{font:700 27px 'Josefin Sans',sans-serif;letter-spacing:1.5px;text-transform:uppercase}
.brand-tag{font:600 12px 'Open Sans',sans-serif;letter-spacing:2.5px;margin-top:2px}
.nav{top:28px;left:560px;display:flex;gap:0}
.nav-item{width:95px;text-align:center;color:var(--white);font:700 12px 'Open Sans',sans-serif;letter-spacing:1px}
.nav-item svg{display:block;margin:0 auto 8px}
.nav-rule{top:104px;left:110px;width:980px;height:1px;background:rgba(255,255,255,.35)}
.hero-title{top:190px;color:var(--white);font:700 58px/1.1 'Josefin Sans',sans-serif;letter-spacing:3px;text-transform:uppercase}
.hero-sub{top:392px;left:400px;width:400px;color:var(--white);text-align:center;font:400 17px/1.4 'Lato',sans-serif;letter-spacing:.5px}
.scroll{top:560px;color:var(--white);font:700 8px 'Open Sans',sans-serif;letter-spacing:1px}

/* services */
.services{top:606px;height:448px;background:var(--dark);color:var(--white)}
.sec-title{font:400 26px 'Lato',sans-serif;letter-spacing:4px;text-transform:uppercase}
.sec-title b{font-weight:700}
.sec-lead{font:400 12px/1.4 'Lato',sans-serif;letter-spacing:.5px}
.blue-rule{top:130px;left:540px;width:120px;height:3px;background:var(--blue)}
.service{position:absolute;top:162px;width:240px;height:222px;text-align:center}
.service.active{border:3px solid var(--blue)}
.service svg{position:absolute;left:80px;top:28px}
.service-name{position:absolute;left:0;width:100%;top:160px;color:var(--blue-text);font:700 20px/1.2 'Open Sans',sans-serif;letter-spacing:2.5px;text-transform:uppercase}

/* portfolio */
.portfolio{top:1054px;height:740px;background:var(--white)}
.portfolio .sec-title{color:#333}
.portfolio .sec-lead{color:#222;font-weight:700;font-size:11px}
.tabs{top:162px;left:280px;width:640px;display:flex;justify-content:space-between;font:700 12px 'Open Sans',sans-serif;letter-spacing:1.5px;color:#c2c2c2;text-transform:uppercase}
.tabs .on{color:#333}
.shot{position:absolute;width:327px;height:186px;border:1px solid #ddd}
.browse-rule{top:686px;left:0;width:1200px;height:2px;background:#5a6f8a}
.browse{top:664px;left:486px;width:228px;height:46px;border-radius:23px;border:2px solid var(--blue);background:var(--white);color:var(--blue);font:700 11px 'Open Sans',sans-serif;letter-spacing:1.5px}

/* solutions */
.solutions{top:1794px;height:441px}
.sol-panel{position:absolute;left:0;top:0;width:555px;height:441px;background:var(--blue);color:var(--white)}
.sol-photo{position:absolute;left:555px;top:0;width:645px;height:441px;background:linear-gradient(160deg,#d7dadf 0%,#c4c7cc 45%,#b4b6b9 100%)}
.sol-title{left:106px;top:24px;font:700 25px/1.3 'Open Sans',sans-serif;letter-spacing:2.5px;text-transform:uppercase}
.sol-item{left:106px;width:420px;display:flex;gap:12px}
.sol-item h4{font:700 12px 'Open Sans',sans-serif;margin-bottom:2px}
.sol-item p{font:400 12px/1.25 'Open Sans',sans-serif}

/* back */
.backup{top:2235px;height:448px;background:linear-gradient(180deg,#54565b,#4a4c51);color:var(--white)}
.backup-title{top:120px;font:700 44px 'Open Sans',sans-serif;letter-spacing:4px;text-transform:uppercase}
.backup-text{top:232px;font:400 23px/1.25 'Open Sans',sans-serif;letter-spacing:1px}

/* testimonial */
.testimonial{top:2683px;height:473px;background:var(--white)}
.client-photo{position:absolute;left:0;top:0;width:475px;height:473px;background:linear-gradient(180deg,#5a86bf,#3f6aa5)}
.client-name{left:22px;top:408px;color:var(--white);font:400 20px 'Lato',sans-serif;letter-spacing:1px}
.client-role{left:22px;top:440px;color:#dfe7f2;font:400 16px 'Lato',sans-serif;letter-spacing:1px}
.t-head{left:475px;width:725px;top:32px;text-align:center;font:400 18px/1.3 'Lato',sans-serif;letter-spacing:1.5px;color:#333;text-transform:uppercase}
.t-head b{font-weight:700}
.t-quote{left:560px;width:555px;top:120px;text-align:center;color:var(--quote);font:italic 700 29px/1.5 'Open Sans',sans-serif}
.t-arrows{left:795px;top:430px}

/* footer */
.site-footer{top:3156px;height:480px;background:var(--footer);color:var(--white)}
.f-col{position:absolute;top:50px}
.f-col h5{font:700 19px 'Lato',sans-serif;letter-spacing:1.5px;text-transform:uppercase;margin-bottom:30px}
.f-col li{list-style:none;font:400 18px 'Lato',sans-serif;color:#d8d8d8;letter-spacing:1px;margin-bottom:24px}
.f-brand{left:850px;top:258px;font:700 22px 'Lato',sans-serif;color:#6a7d96;letter-spacing:.5px}
.f-bar{position:absolute;left:0;top:371px;width:1200px;height:109px;background:var(--footer-bar);border-top:1px solid #2e3038}
.f-copy{left:46px;top:42px;font:400 17px 'Lato',sans-serif;color:#cfcfcf;letter-spacing:.5px}
.f-mark{left:582px;top:36px}
.f-social{left:944px;top:34px;display:flex;gap:10px}
.f-social span{width:36px;height:36px;border-radius:50%;background:#6b6e76;display:block}
</style>
</head>
<body>

<header class="hero">
  <div class="hero-photo" role="img" aria-label="Photo of young colleagues talking and laughing outdoors, tinted blue"></div>
  <div class="brand abs">
    <div class="brand-name">Tidewell Studio</div>
    <div class="brand-tag">EAT | SLEEP | BREATH DIGITAL</div>
  </div>
  <nav class="nav abs">
    <div class="nav-item"><svg width="22" height="16" viewBox="0 0 22 16" fill="#fff"><circle cx="6" cy="4" r="3"/><circle cx="16" cy="4" r="3"/><circle cx="11" cy="5" r="3.4"/><path d="M0 15c0-4 3-6 6-6s6 2 6 6zM10 15c0-4 3-6 6-6s6 2 6 6z"/></svg>ABOUT</div>
    <div class="nav-item"><svg width="18" height="18" viewBox="0 0 18 18"><circle cx="9" cy="9" r="6" fill="none" stroke="#fff" stroke-width="4" stroke-dasharray="3 2.3"/><circle cx="9" cy="9" r="4.5" fill="#fff"/><circle cx="9" cy="9" r="2" fill="#7894b6"/></svg>HOW WE WORK</div>
    <div class="nav-item"><svg width="16" height="18" viewBox="0 0 16 18" fill="#fff"><path d="M2 1h12v12H4a2 2 0 0 0 0 4h10v-1H4a1 1 0 0 1 0-2h10z"/></svg>LEARN</div>
    <div class="nav-item"><svg width="20" height="18" viewBox="0 0 20 18" fill="#fff"><path d="M0 1h4l3 10h10l2-7H6l-.5-2H20v1"/><path d="M5 3h15l-2.5 8H7.5z"/><circle cx="8" cy="15" r="2"/><circle cx="16" cy="15" r="2"/></svg>SHOP</div>
    <div class="nav-item"><svg width="20" height="15" viewBox="0 0 20 15"><rect width="20" height="15" rx="1.5" fill="#fff"/><path d="M1 1l9 7 9-7" fill="none" stroke="#7894b6" stroke-width="1.5"/></svg>CONTACT</div>
  </nav>
  <div class="nav-rule abs"></div>
  <h1 class="hero-title abs center">Want an online<br>presence for your<br>small business?</h1>
  <p class="hero-sub abs">Give your business the exposure it deserves! Get started by ordering services directly from the shop or by shooting us an email</p>
  <a class="btn" style="left:484px;top:483px;width:104px;">Shop</a>
  <a class="btn solid" style="left:600px;top:483px;width:118px;">Contact</a>
  <div class="scroll abs center">
    <svg width="28" height="28" viewBox="0 0 28 28"><circle cx="14" cy="14" r="12.5" fill="none" stroke="#fff" stroke-width="2"/><path d="M8 11l6 6 6-6" fill="none" stroke="#fff" stroke-width="2.5"/></svg>
    <div>LEARN MORE</div>
  </div>
</header>

<section class="services">
  <h2 class="sec-title abs center" style="top:50px;">Our <b>Services</b></h2>
  <p class="sec-lead abs" style="top:90px;left:420px;width:360px;text-align:center;">Lorem ipsum dolor sit amet, consectetur adipiscing elit. Duis consequat quis lectus vel posuere.</p>
  <div class="blue-rule abs"></div>

  <div class="service active" style="left:108px;">
    <svg width="80" height="70" viewBox="0 0 80 70" fill="none" stroke="#fff" stroke-width="3"><rect x="2" y="6" width="62" height="42" rx="2"/><path d="M26 48v10M40 48v10M18 60h30"/><rect x="58" y="26" width="20" height="36" rx="3" fill="#323438"/><path d="M64 56h8"/></svg>
    <div class="service-name">Web Design</div>
  </div>
  <div class="service" style="left:356px;">
    <svg width="80" height="80" viewBox="0 0 80 80" fill="none" stroke="#fff" stroke-width="3"><path d="M12 4h32l12 12v56H12z"/><path d="M44 4v12h12M22 28h24M22 38h24M22 48h14"/><path d="M42 58h22v8a8 8 0 0 1-8 8h-6a8 8 0 0 1-8-8z" fill="#323438"/><path d="M64 61h4a3 3 0 0 1 0 6h-4"/></svg>
    <div class="service-name">Content<br>Marketing</div>
  </div>
  <div class="service" style="left:604px;">
    <svg width="80" height="80" viewBox="0 0 80 80" fill="none" stroke="#fff" stroke-width="3" stroke-linejoin="round"><path d="M40 6l34 16-34 16L6 22z"/><path d="M14 34L6 38l34 16 34-16-8-4"/><path d="M14 50l-8 4 34 16 34-16-8-4"/></svg>
    <div class="service-name">Graphic<br>Design</div>
  </div>
  <div class="service" style="left:852px;">
    <svg width="80" height="80" viewBox="0 0 80 80" fill="none" stroke="#fff" stroke-width="3"><path d="M40 2v6M6 8h68v46H6z"/><path d="M30 54l-8 22M50 54l8 22M40 54v16"/><circle cx="28" cy="22" r="3"/><circle cx="40" cy="22" r="3"/><circle cx="52" cy="22" r="3"/><circle cx="34" cy="32" r="3"/><circle cx="46" cy="32" r="3"/><circle cx="40" cy="42" r="3"/></svg>
    <div class="service-name">Coaching</div>
  </div>
</section>

<section class="portfolio">
  <h2 class="sec-title abs center" style="top:40px;">Port<b>folio</b></h2>
  <p class="sec-lead abs" style="top:84px;left:280px;width:640px;text-align:center;">Lorem ipsum dolor sit amet, consectetur adipiscing elit. Nulla consectetur urna id tortor laoreet, luctus tristique purus tincidunt.</p>
  <div class="tabs abs"><span class="on">Web Design</span><span>Content Marketing</span><span>Graphic Design</span><span>Graphic Design</span></div>

  <div class="shot" role="img" aria-label="Website mockup with colourful blue hero banner" style="left:106px;top:229px;background:linear-gradient(180deg,#4f7fb8,#86a9d2)"></div>
  <div class="shot" role="img" aria-label="Website mockup of a charity running event on dark grey" style="left:439px;top:229px;background:linear-gradient(135deg,#3a3d42,#5b5e63)"></div>
  <div class="shot" role="img" aria-label="Website mockup with dark product photo" style="left:772px;top:229px;background:linear-gradient(180deg,#f4f4f4 0 22%,#1a1a1a 22% 100%)"></div>
  <div class="shot" role="img" aria-label="Dark portfolio website mockup with portrait" style="left:106px;top:431px;background:linear-gradient(90deg,#1c1c1c,#4a4a4a)"></div>
  <div class="shot" role="img" aria-label="Website mockup with snowy mountain scene" style="left:439px;top:431px;background:linear-gradient(180deg,#2c6fb8,#7fb2de 60%,#e8eef5)"></div>
  <div class="shot" role="img" aria-label="Website mockup with autumn outdoor photo" style="left:772px;top:431px;background:linear-gradient(135deg,#6b7a2f,#b98a3a 55%,#5a3a1f)"></div>

  <div class="browse-rule abs"></div>
  <a class="btn browse">Browse our portfolio</a>
</section>

<section class="solutions">
  <div class="sol-panel">
    <h3 class="sol-title abs">We provide solutions<br>for everyone!</h3>
    <div class="sol-item abs" style="top:134px;">
      <svg width="26" height="26" viewBox="0 0 26 26" style="flex:none"><rect x="1" y="3" width="22" height="22" fill="none" stroke="#fff" stroke-width="2"/><path d="M5 13l6 6L25 2" fill="none" stroke="#fff" stroke-width="3"/></svg>
      <div><h4>Tidewell Studio</h4><p>In a world full of JavaScript and CSS, tweets and emojis, pokes and notifications, modern marketing has never seemed more convoluted.</p></div>
    </div>
    <div class="sol-item abs" style="top:230px;">
      <svg width="26" height="26" viewBox="0 0 26 26" style="flex:none"><rect x="1" y="3" width="22" height="22" fill="none" stroke="#fff" stroke-width="2"/><path d="M5 13l6 6L25 2" fill="none" stroke="#fff" stroke-width="3"/></svg>
      <div><h4>Streamlined Marketing Solutions</h4><p>We know the marketing landscape is always changing. We see it every day in fact.<br>And the only way to thrive amidst change is by being willing to adapt.</p></div>
    </div>
    <a class="btn solid" style="left:145px;top:366px;width:142px;">Get Started</a>
    <a class="btn" style="left:300px;top:366px;width:144px;">Learn More</a>
  </div>
  <div class="sol-photo" role="img" aria-label="Photo of a presenter in a red sweater beside a red table at an awards event"></div>
</section>

<section class="backup" role="region" aria-label="Background illustration of a relaxed office desk scene">
  <h2 class="backup-title abs center">We've got your back</h2>
  <p class="backup-text abs center">We'll help you move your business into the digital world,<br>so you can get back to doing what you love.</p>
  <a class="btn solid dark" style="left:450px;top:355px;width:144px;">Get Started</a>
  <a class="btn" style="left:605px;top:355px;width:144px;">Learn More</a>
</section>

<section class="testimonial">
  <div class="client-photo" role="img" aria-label="Portrait photo of a smiling client, tinted blue"></div>
  <div class="client-name abs">Owen Harlow</div>
  <div class="client-role abs">Ceo, Company Name</div>
  <h3 class="t-head abs">See what <b>clients</b> have said about us<br>and our services!</h3>
  <blockquote class="t-quote abs">“Lorem ipsum dolor sit amet, consectetur adipiscing elit. Nunc mauris neque, dignissim sed lobortis eget, euismod ut justo.”</blockquote>
  <svg class="t-arrows abs" width="48" height="24" viewBox="0 0 48 24" fill="none" stroke="#222" stroke-width="4"><path d="M18 3L7 12l11 9M30 3l11 9-11 9"/></svg>
</section>

<footer class="site-footer">
  <div class="f-col" style="left:46px;"><h5>Product</h5><ul><li>Features</li><li>Services</li><li>Products</li><li>Solutions</li></ul></div>
  <div class="f-col" style="left:330px;"><h5>Resources</h5><ul><li>Tidewell Shop</li><li>Inspiration Center</li><li>Success Stories</li><li>Developer Docs</li></ul></div>
  <div class="f-col" style="left:617px;"><h5>Company</h5><ul><li>About</li><li>Careers</li><li>Press</li><li>Contact</li></ul></div>
  <div class="f-col" style="left:899px;"><h5>Support</h5><ul><li>Support Center</li><li>Community</li></ul></div>
  <div class="f-brand abs">tidewell studio</div>
  <div class="f-bar">
    <div class="f-copy abs">© Tidewell Studio, Inc. Terms Privacy Policy</div>
    <svg class="f-mark abs" width="36" height="36" viewBox="0 0 36 36"><circle cx="18" cy="18" r="16" fill="none" stroke="#8a8d94" stroke-width="2"/><path d="M11 24l7-12 7 12" fill="none" stroke="#8a8d94" stroke-width="2"/></svg>
    <div class="f-social abs"><span></span><span></span><span></span><span></span><span></span></div>
  </div>
</footer>

</body>
</html>
```